Personal training and nutrition business needs business card design

We need a business card that outlays our services and invites potential customers to join our team and take the first step to a healthier and more enjoyable life. We cater for any level of fitness and specialize in weight loss and conditioning, strength training, muscle gain and strength endurance. Whether you are just starting off or need some help getting to the next level of your journey we are here to get the job done.
We specialize in one on one or one on two personal training sessions and each program will be custom made to suit individual fitness goals of our clients

```html
<!DOCTYPE html>
<html lang="en">
<head>
<meta charset="utf-8">
<title>Stride &amp; Steady — Business Card</title>
<link href="https://fonts.googleapis.com/css2?family=Exo+2:ital,wght@0,800;1,800&family=Oswald:wght@500&family=Roboto:wght@400&display=swap" rel="stylesheet">
<style>
  :root {
    --bg: #2b2b2c;
    --card: #1c1b1d;
    --emboss: #3a393c;
    --purple: #8a4fb0;
    --purple-deep: #5b3c96;
    --purple-light: #a95aa3;
    --tag: #9d5aa8;
    --text: #ececec;
  }
  * { margin: 0; padding: 0; box-sizing: border-box; }
  html, body { width: 1200px; height: 1138px; overflow: hidden; }
  body { background: var(--bg); font-family: "Roboto", sans-serif; position: relative; }

  .card {
    position: absolute;
    width: 620px; height: 374px;
    background: var(--card);
    border-radius: 14px;
    overflow: hidden;
  }
  .card--front { left: 274px; top: 186px; }
  .card--back  { left: 276px; top: 608px; }

  /* Front */
  .front-name {
    position: absolute; left: 0; right: 0; top: 200px;
    text-align: center;
    font-family: "Exo 2", sans-serif; font-weight: 800;
    font-size: 44px; letter-spacing: 1px;
    color: var(--emboss);
  }
  .tagline {
    font-family: "Oswald", sans-serif; font-weight: 500;
    color: var(--tag); letter-spacing: 1.5px;
    text-transform: uppercase;
  }
  .front-tagline {
    position: absolute; left: 0; right: 0; top: 334px;
    text-align: center; font-size: 13px;
  }

  /* Back */
  .back-waves { position: absolute; inset: 0; width: 620px; height: 374px; }
  .brand-dot {
    position: absolute; left: 118px; top: 56px;
    width: 92px; height: 92px; border-radius: 50%;
    background: linear-gradient(135deg, var(--purple-deep), var(--purple-light));
  }
  .brand-name {
    position: absolute; left: 60px; top: 170px;
    font-family: "Exo 2", sans-serif; font-weight: 800;
    font-size: 34px; line-height: 36px;
    color: var(--text);
  }
  .back-tagline {
    position: absolute; left: 60px; top: 245px;
    font-size: 9px; letter-spacing: 0.8px;
  }
  .edge-tab {
    position: absolute; right: -34px; top: 42px;
    width: 68px; height: 68px; border-radius: 50%;
    background: linear-gradient(135deg, var(--purple), var(--purple-light));
  }
  .person {
    position: absolute; right: 38px; top: 46px; text-align: right;
  }
  .person-name {
    font-family: "Exo 2", sans-serif; font-style: italic; font-weight: 800;
    font-size: 25px; color: var(--purple); letter-spacing: 1px;
    text-transform: uppercase;
  }
  .person-role { font-size: 16px; color: var(--text); margin-top: 2px; }
  .address {
    position: absolute; right: 38px; top: 128px; text-align: right;
    font-size: 16px; line-height: 25px; color: var(--text);
  }
  .contacts {
    position: absolute; right: 26px; top: 278px;
    list-style: none; text-align: right;
    font-size: 15px; line-height: 24px; color: var(--text);
  }
  .contacts li { display: flex; align-items: center; justify-content: flex-end; gap: 12px; }
  .contacts svg { width: 14px; height: 14px; fill: var(--text); }
</style>
</head>
<body>

  <section class="card card--front">
    <div class="front-name">STRIDE &amp; STEADY</div>
    <p class="tagline front-tagline">Personal training.&nbsp; Nutrition. Motivation</p>
  </section>

  <section class="card card--back">
    <svg class="back-waves" viewBox="0 0 620 374" aria-hidden="true">
      <defs>
        <linearGradient id="waveFill" x1="0" y1="1" x2="1" y2="0">
          <stop offset="0" stop-color="#573c94"/>
          <stop offset="1" stop-color="#a85aa2"/>
        </linearGradient>
      </defs>
      <path d="M0,272 C150,330 300,322 450,242 C525,204 585,200 620,212 L620,374 L0,374 Z" fill="url(#waveFill)"/>
      <path d="M0,298 C160,350 320,334 462,258 C532,222 592,220 620,230 L620,246 C590,238 532,240 474,274 C334,350 160,366 0,326 Z" fill="#1c1b1d"/>
      <path d="M48,294 C150,320 260,322 380,286 C300,316 170,318 48,294 Z" fill="#9c56a6"/>
    </svg>

    <div class="brand-dot"></div>
    <div class="brand-name">STRIDE<br>&amp; STEADY</div>
    <p class="tagline back-tagline">Personal training.&nbsp; Nutrition. Motivation</p>

    <div class="edge-tab"></div>
    <div class="person">
      <h1 class="person-name">Mark Rivers</h1>
      <p class="person-role">Personal Trainer</p>
    </div>
    <address class="address" style="font-style:normal">
      418 Cedar Ridge Lane<br>Austin Texas 78701
    </address>

    <ul class="contacts">
      <li>+1 (512) 555-0147
        <svg viewBox="0 0 24 24"><path d="M6.6 10.8a15.1 15.1 0 0 0 6.6 6.6l2.2-2.2a1 1 0 0 1 1-.25 11.4 11.4 0 0 0 3.6.6 1 1 0 0 1 1 1V20a1 1 0 0 1-1 1A17 17 0 0 1 3 4a1 1 0 0 1 1-1h3.5a1 1 0 0 1 1 1c0 1.25.2 2.45.6 3.6a1 1 0 0 1-.25 1z"/></svg>
      </li>
      <li>www.strideandsteady.com
        <svg viewBox="0 0 24 24"><path d="M12 2a10 10 0 1 0 0 20 10 10 0 0 0 0-20zm6.9 6h-3a15.7 15.7 0 0 0-1.4-3.6A8 8 0 0 1 18.9 8zM12 4c.8 1.2 1.5 2.5 1.9 4h-3.8c.4-1.5 1.1-2.8 1.9-4zM4.3 14a8 8 0 0 1 0-4h3.4a16.5 16.5 0 0 0 0 4zm.8 2h3a15.7 15.7 0 0 0 1.4 3.6A8 8 0 0 1 5.1 16zm3-8h-3a8 8 0 0 1 4.4-3.6C8.9 5.5 8.4 6.7 8.1 8zM12 20c-.8-1.2-1.5-2.5-1.9-4h3.8c-.4 1.5-1.1 2.8-1.9 4zm2.3-6H9.7a14.7 14.7 0 0 1 0-4h4.6a14.7 14.7 0 0 1 0 4zm.2 5.6c.6-1.1 1.1-2.3 1.4-3.6h3a8 8 0 0 1-4.4 3.6zM16.3 14a16.5 16.5 0 0 0 0-4h3.4a8 8 0 0 1 0 4z"/></svg>
      </li>
      <li>mark@strideandsteady.com
        <svg viewBox="0 0 24 24"><path d="M2 5h20v14H2zm2 2v.5l8 5 8-5V7zm0 2.8V17h16V9.8l-8 5z"/></svg>
      </li>
    </ul>
  </section>

</body>
</html>
```